Webshop for baby shoes need new design

We are an innovative company selling a one of a kind product on a market with tough competition. We are looking to step up our business and need a new design for our shop.

We are looking for recognition as well as originality. The customer must immediately be able to identify navigation, shopping cart, buy buttons etc. We want warm welcoming colors, but not too strong as to not draw attention away from the products. Retro might be interesting, if "done right".

Suggested color palette: http://huepickerlab.example/#7r2kQmVx9a0b1

We have a logo (attached), but if you have a better idea we might go for that instead. Also, a couple of product images are attached for you to use in the design.

What we do NOT want is a shop that looks like a free template (tradeCart etc). Also, while we are selling baby shoes, we don't want to use the very worn our baby pink/blue scheme, so stay clear of this, thanks.

We suggest that you use this palette, or similar: http://huepickerlab.example/#7r2kQmVx9a0b1

Reason: We feel that we are getting closer to finding a design that we like, but there is still a bit to go. Also we want to give the chance to any late starters to show their idea. The competition is still open.

Target Market(s)

babies and their parents

Industry/Entity Type

Shopping

Requirements
Must have
• The usual webshop elements
- shopping cart
- product listing
- product page
- buy buttons
Nice to have
• - large footer area for links, info and function (see vimlo.example for an example)
- some kind of product navigation/filter (left, top or right)
- place for promotion banners

```html
<!DOCTYPE html>
<html lang="en">
<head>
<meta charset="utf-8">
<title>Tossabo – Children's Fitted Footwear</title>
<link href="https://fonts.googleapis.com/css2?family=Libre+Baskerville:wght@400;700&family=Arimo:wght@400;700&family=Parisienne&display=swap" rel="stylesheet">
<style>
:root{
  --brown-deep:#5a2811;
  --brown:#7a3a1a;
  --brown-mid:#9a5a2e;
  --nav-red:#7d2416;
  --nav-red-dark:#5e170d;
  --tan:#d6bd93;
  --tan-light:#efe2c8;
  --cream:#f6eddc;
  --cta-red:#b3141a;
  --teal:#2d7a6e;
  --wine:#7d1f2a;
  --ink:#3a2a20;
  --muted:#7d6e62;
  --line:#d9d2cb;
  --card-bg:#ffffff;
  --footer-bg:#f0edeb;
  --footer-bar:#6a3312;
}
*{box-sizing:border-box;margin:0;padding:0}
html,body{width:960px;height:1200px;overflow:hidden;background:#fff}
body{position:relative;font-family:'Arimo',Arial,sans-serif;color:var(--ink)}
.abs{position:absolute}

/* header */
.brand{left:108px;top:14px;display:flex;align-items:center;gap:12px}
.brand-mark{width:50px;height:50px;background:var(--brown-mid);border-radius:6px}
.brand-name{font-family:'Libre Baskerville',Georgia,serif;font-weight:700;font-size:40px;color:var(--brown)}
.basket{left:601px;top:8px;width:257px;height:75px;background:var(--tan-light);border:1px solid #e4d2b3;border-radius:5px;padding:8px 10px;box-shadow:0 1px 3px rgba(0,0,0,.12)}
.basket h2{font-family:'Arimo',sans-serif;font-weight:400;font-size:17px;color:#9a7c58}
.basket .count{font-size:8.5px;color:#a08868;margin-top:1px}
.basket .total{position:absolute;left:12px;bottom:9px;font-size:8.5px;color:#8a6a48;font-weight:700}
.basket .account{position:absolute;right:10px;top:16px;font-size:8.5px;color:#8a6a48}
.basket .view{position:absolute;right:10px;bottom:9px;font-size:8.5px;color:#a08868;display:flex;align-items:center;gap:6px}

/* navigation */
.nav{left:93px;top:93px;width:774px;height:54px;background:var(--tan);border-radius:10px;padding:6px}
.nav-inner{height:100%;background:linear-gradient(#8a2b1a,var(--nav-red-dark));border-radius:6px;border:1px dashed rgba(230,190,150,.45);position:relative;display:flex;align-items:center}
.nav a{font-family:'Libre Baskerville',Georgia,serif;font-size:16px;color:var(--cream);text-decoration:none;position:absolute;top:11px}
.nav .home{left:4px;top:2px;width:92px;height:36px;background:linear-gradient(#a2532e,#6d2a14);border-radius:3px;display:flex;align-items:center;justify-content:center}
.search{position:absolute;left:587px;top:8px;width:162px;height:22px;background:#cfb487;border-radius:4px}
.search span{position:absolute;right:4px;top:3px;width:16px;height:16px;border-radius:4px;background:#e6d6b8}

/* hero */
.hero{left:93px;top:153px;width:774px;height:259px;border-radius:6px;background:radial-gradient(ellipse at 60% 50%,#a86a3e,#6a3316 75%);border:3px solid #7a3a1a;overflow:hidden}
.hero-photo{position:absolute;left:370px;top:6px;width:390px;height:245px;border-radius:40% 45% 20% 20%;background:radial-gradient(ellipse at 55% 55%,#2f4a80,#203462 60%,rgba(32,52,98,0) 72%)}
.hero h1{position:absolute;font-family:'Libre Baskerville',Georgia,serif;font-weight:700;color:#f1e2cc;line-height:1}
.hero .q{left:27px;top:24px;font-size:34px}
.hero .d{left:71px;top:67px;font-size:34px}
.hero .f{left:24px;top:111px;font-size:50px;color:#f4d9bd}
.hero p{position:absolute;left:25px;top:174px;font-family:'Libre Baskerville',Georgia,serif;font-weight:700;font-size:15.5px;color:#f6ead8}
.cta{position:absolute;left:25px;top:213px;width:174px;height:24px;background:linear-gradient(#c8252a,#8e0e12);border-radius:3px;color:#fff;font-family:'Libre Baskerville',Georgia,serif;font-size:11.5px;display:flex;align-items:center;padding-left:13px;gap:14px}
.arrow-dot{width:16px;height:16px;border-radius:50%;background:#fff;display:flex;align-items:center;justify-content:center}

/* filter sidebar */
.filter{left:92px;top:428px;width:164px;height:522px;border:1px solid var(--line);border-radius:5px;padding:10px 0 0 18px;font-size:9px}
.filter h3{font-size:10.5px;font-weight:700;margin:0 0 10px 2px}
.filter .group{width:100px;border-top:1px dotted #c9c2bb;padding:5px 0 4px}
.filter .label{color:#333;margin-bottom:3px}
.filter a{display:block;color:#2e2a6e;text-decoration:underline;line-height:11.6px;font-size:9px}
.select{width:94px;height:14px;border:1px solid #aaa;font-size:9px;color:#777;padding-left:3px;line-height:12px;position:relative;margin:2px 0 3px}
.select::after{content:"";position:absolute;right:0;top:0;width:12px;height:12px;border-left:1px solid #aaa;background:linear-gradient(#fff,#ddd)}

/* promo tiles */
.promo{top:428px;height:166px;border-radius:4px;overflow:hidden}
.promo .head{height:28px;display:flex;align-items:center;justify-content:space-between;padding:0 10px 0 18px;font-family:'Libre Baskerville',Georgia,serif;font-size:15px;color:#fff}
.promo .pic{position:absolute;left:4px;right:4px;top:30px;bottom:4px;border-radius:2px}
.promo.new{left:288px;width:187px;background:var(--wine)}
.promo.new .pic{background:radial-gradient(ellipse,#d4dbe8,#ffffff 70%)}
.promo.offer{left:485px;width:187px;background:var(--teal)}
.promo.offer .pic{background:radial-gradient(ellipse at 55% 60%,#d9a06a,#b97236)}
.promo.service{left:680px;width:187px;background:linear-gradient(135deg,#b9652c,#8a3e17);border:1px dashed #f0c79a}
.service .script{position:absolute;left:20px;top:10px;font-family:'Parisienne',cursive;font-size:23px;line-height:23.5px;color:#fbeedd}
.service .badge{position:absolute;left:125px;top:4px;width:62px;height:62px;border-radius:50%;background:#5a2a12;color:#f2dcc0;font-family:'Libre Baskerville',serif;font-weight:700;font-size:21px;display:flex;align-items:center;justify-content:center}
.service .locator{position:absolute;left:36px;top:134px;width:125px;height:18px;background:var(--cta-red);border-radius:2px;color:#fff;font-family:'Libre Baskerville',serif;font-size:9px;font-weight:700;display:flex;align-items:center;justify-content:center}

/* product grid */
.section-title{left:295px;top:607px;font-family:'Libre Baskerville',Georgia,serif;font-weight:700;font-size:15.5px;color:#6a3316}
.card{width:143px;height:148px;background:var(--card-bg);border:1px solid var(--line);border-radius:4px;box-shadow:0 1px 2px rgba(0,0,0,.06)}
.card .shot{position:absolute;left:24px;top:8px;width:95px;height:68px;border-radius:40% 40% 18% 18%}
.shot.navy{background:radial-gradient(ellipse at 50% 60%,#2d4579,#4a6aa0 55%,rgba(255,255,255,0) 72%)}
.shot.ivory{background:radial-gradient(ellipse at 50% 60%,#e5ddc8,#f2ede0 55%,rgba(255,255,255,0) 72%)}
.shot.teal{background:radial-gradient(ellipse at 50% 60%,#2a5f78,#3d7c92 55%,rgba(255,255,255,0) 72%)}
.card .name{position:absolute;left:12px;top:85px;font-size:12px;color:#333}
.card .price{position:absolute;right:12px;top:85px;font-size:12px;color:#222}
.card .type{position:absolute;left:12px;top:100px;font-size:8.5px;color:#777}
.card .buy{position:absolute;left:31px;top:124px;width:87px;height:16px;background:linear-gradient(#7a3518,#4e1e0a);border-radius:8px;color:#fff;font-size:9px;display:flex;align-items:center;padding-left:8px;gap:10px}
.card .buy i{width:14px;height:14px;border-radius:50%;background:#fff;color:#5a2811;font-style:normal;font-weight:700;font-size:12px;line-height:14px;text-align:center}

/* footer */
.footer{left:0;top:987px;width:960px;height:163px;background:linear-gradient(#fdfcfb,var(--footer-bg));border-top:3px solid #a46a45}
.foot-col{top:1005px}
.foot-col h4{font-family:'Libre Baskerville',Georgia,serif;font-size:10.5px;color:#7a3a1a;margin-bottom:8px}
.foot-col a{display:block;font-size:9px;color:#8a4a22;text-decoration:none;line-height:17.8px;letter-spacing:.2px}
.foot-brand{left:625px;top:1008px;display:flex;flex-direction:column;align-items:center;gap:8px}
.foot-brand .brand-mark{width:58px;height:58px}
.foot-brand .brand-name{font-size:40px}
.socials{left:778px;top:1123px;display:flex;gap:5px}
.socials span{width:14px;height:14px;border-radius:3px;background:#8a7a70}
.bar{left:0;top:1150px;width:960px;height:50px;background:var(--footer-bar);color:#f3e6d6;font-size:9px;padding:18px 0 0 94px}
</style>
</head>
<body>

<header>
  <div class="abs brand"><span class="brand-mark"></span><span class="brand-name">Tossabo</span></div>
  <div class="abs basket">
    <h2>Your Basket</h2>
    <div class="count">0 items</div>
    <div class="account">Register / Log in</div>
    <div class="total">Total: 0.00</div>
    <div class="view">
      <svg width="11" height="11" viewBox="0 0 11 11"><path d="M5.5 1v6M3 4.5l2.5 2.5 2.5-2.5M1.5 9.5h8" stroke="#a08868" stroke-width="1.4" fill="none"/></svg>
      view basket
    </div>
  </div>
</header>

<nav class="abs nav">
  <div class="nav-inner">
    <a class="home" href="#">Home</a>
    <a href="#" style="left:126px">Girls</a>
    <a href="#" style="left:197px">Boys</a>
    <a href="#" style="left:260px">Store Locator</a>
    <a href="#" style="left:388px">Fitting</a>
    <a href="#" style="left:472px">About Us</a>
    <div class="search"><span></span></div>
  </div>
</nav>

<section class="abs hero">
  <div class="hero-photo" role="img" aria-label="Photo of two leather toddler boots, navy with orange trim and a teal velcro boot"></div>
  <h1 class="q">Quality &amp;</h1>
  <h1 class="d">Durability</h1>
  <h1 class="f">Fit &amp; Style</h1>
  <p>Experts in Childrens fitted footwear</p>
  <div class="cta">SEE OUR COLECTION <span class="arrow-dot"><svg width="8" height="8" viewBox="0 0 8 8"><path d="M2.5 1l3 3-3 3" stroke="#b3141a" stroke-width="1.6" fill="none"/></svg></span></div>
</section>

<aside class="abs filter">
  <h3>narrow by:</h3>
  <div class="group"><div class="label">special offers</div><a href="#">Sale only</a></div>
  <div class="group"><div class="label">category</div>
    <a href="#">Boots</a><a href="#">Canvas</a><a href="#">English Classics</a><a href="#">First Walking Shoes</a><a href="#">Non-school Shoes</a><a href="#">Pre-walkers</a><a href="#">Sandals</a><a href="#">School Shoes</a><a href="#">Trainers</a><a href="#">Wellies</a>
  </div>
  <div class="group"><div class="label">gender</div><a href="#">Boys</a><a href="#">Boys &amp; Girls</a></div>
  <div class="group"><div class="label">sizes</div><div class="select">Please select</div></div>
  <div class="group"><div class="label">fit</div><div class="select">Please select</div></div>
  <div class="group"><div class="label">colour</div><div class="select">Please select</div></div>
  <div class="group"><div class="label">styling</div>
    <a href="#">Closed Shoe</a><a href="#">Buckle</a><a href="#">Laces</a><a href="#">Riptape</a><a href="#">Slip-on</a><a href="#">T-bars</a><a href="#">Zip</a>
  </div>
</aside>

<div class="abs promo new">
  <div class="head">New Arrivals <span class="arrow-dot"><svg width="8" height="8" viewBox="0 0 8 8"><path d="M2.5 1l3 3-3 3" stroke="#7d1f2a" stroke-width="1.6" fill="none"/></svg></span></div>
  <div class="pic" role="img" aria-label="Photo of a navy and light blue lace-up baby shoe"></div>
</div>
<div class="abs promo offer">
  <div class="head">Special Offers <span class="arrow-dot"><svg width="8" height="8" viewBox="0 0 8 8"><path d="M2.5 1l3 3-3 3" stroke="#2d7a6e" stroke-width="1.6" fill="none"/></svg></span></div>
  <div class="pic" role="img" aria-label="Photo of red and white baby sneakers with wooden toys on a table"></div>
</div>
<div class="abs promo service">
  <div class="script">Our<br>Customers<br>rate our<br>excellent<br>service</div>
  <div class="badge">95%</div>
  <div class="locator">STORE LOCATOR</div>
</div>

<h2 class="abs section-title">Winter Collection</h2>

<div class="abs card" style="left:288px;top:639px"><div class="shot navy" role="img" aria-label="Navy boot with orange trim"></div><span class="name">shoe title</span><span class="price">$ 120</span><span class="type">type</span><span class="buy">Add To Cart <i>+</i></span></div>
<div class="abs card" style="left:434px;top:639px"><div class="shot navy" role="img" aria-label="Navy lace-up baby shoe"></div><span class="name">shoe title</span><span class="price">$ 120</span><span class="type">type</span><span class="buy">Add To Cart <i>+</i></span></div>
<div class="abs card" style="left:579px;top:639px"><div class="shot ivory" role="img" aria-label="Ivory leather baby shoe"></div><span class="name">shoe title</span><span class="price">$ 120</span><span class="type">type</span><span class="buy">Add To Cart <i>+</i></span></div>
<div class="abs card" style="left:724px;top:639px"><div class="shot teal" role="img" aria-label="Teal velcro baby boot"></div><span class="name">shoe title</span><span class="price">$ 120</span><span class="type">type</span><span class="buy">Add To Cart <i>+</i></span></div>

<div class="abs card" style="left:288px;top:802px"><div class="shot navy" role="img" aria-label="Navy boot with orange trim"></div><span class="name">shoe title</span><span class="price">$ 120</span><span class="type">type</span><span class="buy">Add To Cart <i>+</i></span></div>
<div class="abs card" style="left:434px;top:802px"><div class="shot ivory" role="img" aria-label="Ivory leather baby shoe"></div><span class="name">shoe title</span><span class="price">$ 120</span><span class="type">type</span><span class="buy">Add To Cart <i>+</i></span></div>
<div class="abs card" style="left:579px;top:802px"><div class="shot navy" role="img" aria-label="Navy lace-up baby shoe"></div><span class="name">shoe title</span><span class="price">$ 120</span><span class="type">type</span><span class="buy">Add To Cart <i>+</i></span></div>
<div class="abs card" style="left:724px;top:802px"><div class="shot teal" role="img" aria-label="Teal velcro baby boot"></div><span class="name">shoe title</span><span class="price">$ 120</span><span class="type">type</span><span class="buy">Add To Cart <i>+</i></span></div>

<footer>
  <div class="abs footer"></div>
  <div class="abs foot-col" style="left:98px"><h4>WHY SHOP WITH US?</h4>
    <a href="#">Free shipping</a><a href="#">Free return</a><a href="#">14 day right of return</a><a href="#">Large selection</a><a href="#">Accessible Customer Service</a><a href="#">Pay by invoice</a></div>
  <div class="abs foot-col" style="left:254px"><h4>WHAT'S IN STORE?</h4>
    <a href="#">Kids Shoes</a><a href="#">Summer collection</a><a href="#">Shoe</a><a href="#">Footwear brands AZ</a></div>
  <div class="abs foot-col" style="left:426px"><h4>MORE INFORMATION</h4>
    <a href="#">About Us</a><a href="#">Safety</a><a href="#">Terms and conditions</a><a href="#">Shipping Terms</a><a href="#">Become an affiliate</a></div>
  <div class="abs foot-brand"><span class="brand-mark"></span><span class="brand-name">Tossabo</span></div>
  <div class="abs socials"><span></span><span></span><span></span><span></span></div>
  <div class="abs bar">Copyright © Tossabo Shoes Ltd. 2012 All rights reserved</div>
</footer>

</body>
</html>
```